Onboarding Infographic/brochure

We are a small criminal defense firm looking to create some sort of infographic or brochure that we can onboard new clients with. We are currently sending it out via email but want something a bit cooler and fun to send to clients. The information is:

A Few Quick Rules

We are here to help each step of the way. While questions are never discouraged, this letter will answer some of the most common ones we get asked.

Communications

As a client, you should always be in the loop. While we will try to respond to questions as quickly as possible, sometimes we are unable to respond right away. Do not worry - we promise to get back to you soon. Some questions might take some time to research, and a correct answer is better than a quick one.

Appointments

One of the benefits of having an attorney is the ability to discuss your case outside of court, minus the stress and headaches. If you need an appointment, please contact the office.

Appointments must be scheduled in advance. We do not want you to make a special trip to the office only to learn that we are in court or otherwise unavailable.

Jail Visits

If your family member is currently in jail, we take that very seriously. We will visit your loved one and introduce ourselves. While the case is ongoing, we ask that a family member be designated a “contact” person so that messages can be relayed quickly. Never discuss the facts of the case over the phone with someone who is in jail. Jail calls are recorded and we have seen too many cases go south based on remarks made over recorded lines.

Police Reports and Discovery

We will do our best to provide you with copies of everything we receive on your case. Most information will be emailed, so please keep your email address up to date.

Changes in Contact Information

If you move or change numbers during the case, please let us know. It is difficult to help if we are unable to reach you, and helping you is why we are here.

Court Appearances

Cases do not get resolved as quickly as they do on television. Expect there to be several hearings in your case and it may be necessary for you to attend one or more of them. If a hearing is set, you will receive notice of the date and time of each hearing.

Billing and Collections

We understand that this investment was a huge decision for you. As we focus on providing the best representation, we will need for you to stay on schedule with any payment arrangements agreed to at the time of your initial consultation.

Again, thank you for your trust in us. We look forward to getting a fantastic outcome on your case.

Target Market(s)

Criminal defense clients and their families

Industry/Entity Type

Legal

Font styles to use
Serif

Requirements
Must have
• Must incorporate all of the rules we email out. Would like diagrams, images or pictures
Nice to have
• We attached a Welcome brochure. Not sure I want it to look super similar, hence the request for infographic.

```html
<!DOCTYPE html>
<html lang="en">
<head>
<meta charset="utf-8">
<title>A Few Quick Rules – Veritas Law Partners</title>
<link rel="stylesheet" href="https://fonts.googleapis.com/css2?family=Montserrat:wght@400;500;600;700;800&family=Oswald:wght@700&family=Poppins:wght@200;600;700&display=swap">
<style>
  :root {
    --navy-deep: #0f1f3d;
    --navy: #1d3866;
    --navy-badge: #1f3e73;
    --band: #1e3f7a;
    --blue-head: #2f73c6;
    --blue-title: #8fb0e0;
    --ink: #1c1c1c;
    --white: #ffffff;
    --dash: #b9c0cc;
    --stone-light: #e6d7b8;
    --stone-dark: #8a7452;
  }
  * { margin: 0; padding: 0; box-sizing: border-box; }
  html, body { width: 1200px; height: 2201px; overflow: hidden; background: var(--white); }
  .sheet { position: relative; width: 1200px; height: 2201px; overflow: hidden; background: var(--white); font-family: "Montserrat", sans-serif; color: var(--ink); }

  .hero { position: absolute; left: 0; top: 0; width: 1200px; height: 800px; }

  .brand { position: absolute; left: 95px; top: 92px; color: var(--white); font-family: "Montserrat", sans-serif; font-weight: 800; }
  .brand-main { font-size: 62px; line-height: 1; letter-spacing: -1px; }
  .brand-sub { font-size: 22px; letter-spacing: 12px; margin-top: 4px; }

  .title-light { position: absolute; left: 93px; top: 228px; font-family: "Poppins", sans-serif; font-weight: 200; font-size: 78px; letter-spacing: 8px; color: var(--white); line-height: 1; }
  .title-bold { position: absolute; left: 93px; top: 306px; font-family: "Oswald", sans-serif; font-weight: 700; font-size: 82px; color: var(--blue-title); line-height: 1; letter-spacing: 1px; }
  .intro { position: absolute; left: 94px; top: 400px; width: 410px; font-size: 22px; line-height: 27px; color: var(--white); font-weight: 500; }

  .divider-v { position: absolute; width: 0; border-left: 2px dashed var(--dash); }
  .divider-h { position: absolute; height: 0; border-top: 2px dashed var(--dash); }

  .art { position: absolute; border-radius: 24px; }
  .badge { position: absolute; width: 46px; height: 46px; border-radius: 50%; background: var(--navy-badge); color: var(--white); font-family: "Poppins", sans-serif; font-weight: 700; font-size: 21px; display: flex; align-items: center; justify-content: center; }
  .rule-title { position: absolute; font-family: "Poppins", sans-serif; font-weight: 700; font-size: 27px; line-height: 32px; color: var(--blue-head); }
  .rule-text { position: absolute; font-size: 16.6px; line-height: 21px; color: var(--ink); }
  .rule-text p + p { margin-top: 21px; }

  .contact-phone { position: absolute; left: 110px; top: 1982px; display: flex; align-items: center; gap: 10px; font-family: "Poppins", sans-serif; font-weight: 700; font-size: 38px; color: var(--ink); line-height: 1; }
  .contact-address { position: absolute; left: 498px; top: 1988px; display: flex; align-items: center; gap: 10px; font-size: 18px; line-height: 22px; font-weight: 500; }
  .website { position: absolute; left: 109px; top: 2043px; width: 665px; height: 40px; border-radius: 20px; background: var(--navy); display: flex; align-items: center; justify-content: center; gap: 12px; font-family: "Montserrat", sans-serif; font-weight: 800; }
  .website-label { color: var(--blue-title); font-size: 19px; }
  .website-url { color: var(--white); font-size: 21px; letter-spacing: 1.5px; }

  .bottom-band { position: absolute; left: 0; top: 2170px; width: 1200px; height: 31px; background: var(--band); }
</style>
</head>
<body>
<main class="sheet">

  <svg class="hero" viewBox="0 0 1200 800" xmlns="http://www.w3.org/2000/svg">
    <defs>
      <linearGradient id="heroBg" x1="0" y1="0" x2="1" y2="1">
        <stop offset="0" stop-color="#13264a"/>
        <stop offset="0.5" stop-color="#1d3866"/>
        <stop offset="1" stop-color="#0e1a33"/>
      </linearGradient>
      <linearGradient id="stone" x1="0" y1="0" x2="1" y2="1">
        <stop offset="0" stop-color="#c9b189"/>
        <stop offset="0.5" stop-color="#e6d7b8"/>
        <stop offset="1" stop-color="#9c8460"/>
      </linearGradient>
    </defs>
    <rect width="1200" height="800" fill="url(#heroBg)"/>
    <polygon role="img" aria-label="Photo of a classical courthouse roof and columns seen from below"
             points="887,141 1200,303 1200,800 369,800 369,667" fill="url(#stone)"/>
    <path d="M0,660 C70,700 190,640 284,600 C380,570 420,700 498,715 C590,730 630,790 673,777 C720,760 750,620 799,610 C860,600 880,720 916,720 C980,720 1060,650 1200,638 L1200,800 L0,800 Z" fill="#ffffff"/>
  </svg>

  <div class="brand">
    <div class="brand-main">VERITAS</div>
    <div class="brand-sub">LAW PARTNERS</div>
  </div>
  <h1>
    <span class="title-light">A FEW</span>
    <span class="title-bold">QUICK RULES</span>
  </h1>
  <p class="intro">We are here to help each step of the way. While questions are never discouraged, this letter will answer some of the most common ones we get asked.</p>

  <div class="divider-v" style="left:405px; top:748px; height:1154px;"></div>
  <div class="divider-v" style="left:796px; top:748px; height:1331px;"></div>

  <!-- Rule 01 -->
  <div class="art" role="img" aria-label="Illustration of connected people standing on teal platforms" style="left:105px; top:662px; width:247px; height:250px; background:radial-gradient(circle, #d9f1f1 0%, #ffffff 75%);"></div>
  <div class="badge" style="left:105px; top:893px;">01</div>
  <h2 class="rule-title" style="left:105px; top:948px;">Communications</h2>
  <div class="rule-text" style="left:105px; top:999px; width:265px;">As a client, you should always be in the loop. While we will try to respond to questions as quickly as possible, sometimes we are unable to respond right away. Do not worry - we promise to get back to you soon. Some questions might take some time to research, and a correct answer is better than a quick one.</div>
  <div class="divider-h" style="left:105px; top:1257px; width:276px;"></div>

  <!-- Rule 02 -->
  <div class="art" role="img" aria-label="Illustration of a person scheduling on a large phone calendar beside a clock and plants" style="left:105px; top:1280px; width:247px; height:232px; background:linear-gradient(135deg, #d8f3f5, #a9d8f0 60%, #f5c64a);"></div>
  <div class="badge" style="left:105px; top:1502px;">02</div>
  <h2 class="rule-title" style="left:105px; top:1567px;">Appointments</h2>
  <div class="rule-text" style="left:105px; top:1613px; width:270px;">
    <p>One of the benefits of having an attorney is the ability to discuss your case outside of court, minus the stress and headaches. If you need an appointment, please contact the office.</p>
    <p>Appointments must be scheduled in advance. We do not want you to make a special trip to the office only to learn that we are in court or otherwise unavailable.</p>
  </div>

  <!-- Rule 03 -->
  <div class="art" role="img" aria-label="Illustration of a family visiting a jail with an officer in front of prison bars" style="left:420px; top:801px; width:355px; height:235px; background:linear-gradient(180deg, #eef0ff, #b8bfe8 60%, #f2c23d);"></div>
  <div class="badge" style="left:686px; top:1051px;">03</div>
  <h2 class="rule-title" style="left:452px; top:1082px;">Jail Visits</h2>
  <div class="rule-text" style="left:452px; top:1121px; width:325px;">If your family member is currently in jail, we take that very seriously. We will visit your loved one and introduce ourselves. While the case is ongoing, we ask that a family member be designated a “contact” person so that messages can be relayed quickly. Never discuss the facts of the case over the phone with someone who is in jail. Jail calls are recorded and we have seen too many cases go south based on remarks made over recorded lines.</div>
  <div class="divider-h" style="left:452px; top:1435px; width:312px;"></div>

  <!-- Rule 04 -->
  <div class="art" role="img" aria-label="Illustration of police report documents, an officer cap, handcuffs and detectives" style="left:435px; top:1466px; width:325px; height:206px; background:linear-gradient(180deg, #dceefa, #6fb3e6 55%, #3f3b4f);"></div>
  <div class="badge" style="left:686px; top:1692px;">04</div>
  <h2 class="rule-title" style="left:452px; top:1699px;">Police Reports<br>and Discovery</h2>
  <div class="rule-text" style="left:452px; top:1782px; width:305px;">We will do our best to provide you with copies of everything we receive on your case. Most information will be emailed, so please keep your email address up to date.</div>

  <!-- Rule 05 -->
  <div class="art" role="img" aria-label="Illustration of a mailbox, envelope, telephone and people sending messages" style="left:828px; top:739px; width:306px; height:160px; background:linear-gradient(135deg, #e3f1fb, #f4b43a 45%, #1e5fe0);"></div>
  <div class="badge" style="left:834px; top:893px;">05</div>
  <h2 class="rule-title" style="left:837px; top:946px;">Changes in<br>Contact Information</h2>
  <div class="rule-text" style="left:837px; top:1019px; width:285px;">If you move or change numbers during the case, please let us know. It is difficult to help if we are unable to reach you, and helping you is why we are here.</div>
  <div class="divider-h" style="left:837px; top:1161px; width:288px;"></div>

  <!-- Rule 06 -->
  <div class="art" role="img" aria-label="Illustration of three judges seated behind a wooden court bench" style="left:828px; top:1179px; width:300px; height:150px; background:linear-gradient(180deg, #f4f4f6, #c98d5e 55%, #a8663a);"></div>
  <div class="badge" style="left:834px; top:1304px;">06</div>
  <h2 class="rule-title" style="left:837px; top:1356px;">Court Appearances</h2>
  <div class="rule-text" style="left:837px; top:1396px; width:290px;">Cases do not get resolved as quickly as they do on television. Expect there to be several hearings in your case and it may be necessary for you to attend one or more of them. If a hearing is set, you will receive notice of the date and time of each hearing.</div>
  <div class="divider-h" style="left:837px; top:1605px; width:288px;"></div>

  <!-- Rule 07 -->
  <div class="art" role="img" aria-label="Illustration of people around a large invoice with coins and a calculator" style="left:835px; top:1614px; width:290px; height:163px; background:linear-gradient(135deg, #e6effb, #b9cdf2 55%, #f2a93b);"></div>
  <div class="badge" style="left:834px; top:1768px;">07</div>
  <h2 class="rule-title" style="left:837px; top:1823px;">Billing and<br>Collections</h2>
  <div class="rule-text" style="left:837px; top:1899px; width:290px;">We understand that this investment was a huge decision for you. As we focus on providing the best representation, we will need for you to stay on schedule with any payment arrangements agreed to at the time of your initial consultation.</div>

  <!-- Contact -->
  <div class="contact-phone">
    <svg width="40" height="40" viewBox="0 0 24 24" aria-hidden="true"><path d="M6.6 10.8a15.1 15.1 0 0 0 6.6 6.6l2.2-2.2a1 1 0 0 1 1-.25 11.4 11.4 0 0 0 3.6.57 1 1 0 0 1 1 1V20a1 1 0 0 1-1 1A17 17 0 0 1 3 4a1 1 0 0 1 1-1h3.5a1 1 0 0 1 1 1c0 1.25.2 2.45.57 3.57a1 1 0 0 1-.25 1z" fill="none" stroke="#1d3866" stroke-width="1.8"/><path d="M15 3.5a6 6 0 0 1 5.5 5.5M15 7a2.5 2.5 0 0 1 2 2" fill="none" stroke="#1d3866" stroke-width="1.8" stroke-linecap="round"/></svg>
    <span>(555) 014-2290</span>
  </div>
  <div class="contact-address">
    <svg width="28" height="38" viewBox="0 0 24 32" aria-hidden="true"><path d="M12 0a12 12 0 0 0-12 12c0 9 12 20 12 20s12-11 12-20A12 12 0 0 0 12 0z" fill="#1d3866"/><circle cx="12" cy="12" r="4.5" fill="#fff"/></svg>
    <span>410 W Cedar St #112<br>Riverton, California 90210</span>
  </div>
  <div class="website">
    <span class="website-label">VISIT OUR WEBSITE:</span>
    <span class="website-url">www.veritaslawpartners.com</span>
  </div>

  <div class="bottom-band"></div>
</main>
</body>
</html>
```